Cans for flavored Macadamias

Brindle Ridge Orchard Nut Company (www.brindleridge-example.com) has been packaging 3 flavors of macadamia nuts in to 200g pouches for a number of years. We are about to change from 200g pouches to 80g cans. We need a fresh new look although the back ground colours must stay the same, Roasted & Salted = Yellow, Wasabi = Green, Abalone = Blue.
The can label and lid sticker will be printed 4 colour process. The trimmed finished sizes are, can label - L246 x H60mm and lid sticker 61mm diameter. The attached files show the existing front and back labels for the pouches. The health benefits, ingredients and nutrition facts information can used. Delete address and bar code but leave space for new ones. '80g Net' must show on the front of the can label. Product of Australia logo must be prominent on both can label and lid sticker.
The general feeling is we need to have a photo of a koala on there somewhere, maybe the lid. I have uploaded a photo that I hope you can use.
Updates

Target Market(s)

We're in all of Australia's duty free stores and a lot of souvenir stores. We do sell in to retails. Our target customers are primarily Asian hence the Wasabi and Abalone flavours.

Industry/Entity Type

It Company

Requirements
Must have
• If you google images for "buy Australian flavoured macadamias" it shows most of what's currently on the market. We obviously don't want to look the same as any of them.

```html
<!DOCTYPE html>
<html lang="en">
<head>
<meta charset="utf-8">
<title>Macadamia Nut Can Labels</title>
<link rel="stylesheet" href="https://fonts.googleapis.com/css2?family=Arimo:wght@400;700&family=Roboto+Condensed:wght@400;700&family=Gochi+Hand&family=Chewy&family=Fredoka:wght@600&display=swap">
<style>
  :root{
    --page:#f4f4f2;
    --ink:#1a1a1a;
    --title-orange:#e8642a;
    --title-navy:#1d3f8f;
    --cream:#f3e2b4;
    --tan:#d3a45c;

    --wasabi-bg:#5cc79f;
    --wasabi-bg-dark:#3fa57f;
    --wasabi-stripe:#1e7a3c;
    --wasabi-panel:#9fd86b;
    --wasabi-ribbon:#7cc242;
    --wasabi-ribbon-dark:#2f8a3a;
    --wasabi-dot:#1e6b36;

    --abalone-bg:#3f82b0;
    --abalone-bg-dark:#2c6591;
    --abalone-stripe:#2aa3e0;
    --abalone-panel:#35a9e2;
    --abalone-ribbon:#2b9bda;
    --abalone-ribbon-dark:#1b3f8a;
    --abalone-dot:#3b5cb0;

    --salted-bg:#f6e43c;
    --salted-bg-dark:#e6cf2a;
    --salted-stripe:#f39a1e;
    --salted-panel:#f39a24;
    --salted-ribbon:#f6a52c;
    --salted-ribbon-dark:#d9801b;
    --salted-dot:#a35a1d;
  }
  *{box-sizing:border-box;margin:0;padding:0}
  html,body{width:1200px;height:996px;overflow:hidden;background:var(--page)}
  body{font-family:"Arimo",Arial,sans-serif;color:var(--ink);position:relative}

  .label{
    position:absolute;left:50px;width:1100px;height:268px;overflow:hidden;
    background:linear-gradient(100deg,var(--bg) 0%,var(--bg-dark) 45%,var(--bg) 100%);
    box-shadow:0 6px 14px rgba(0,0,0,.25);
  }
  .label--wasabi{top:48px;--bg:var(--wasabi-bg);--bg-dark:var(--wasabi-bg-dark);--stripe:var(--wasabi-stripe);--panel:var(--wasabi-panel);--ribbon:var(--wasabi-ribbon);--ribbon-dark:var(--wasabi-ribbon-dark);--dot:var(--wasabi-dot)}
  .label--abalone{top:364px;--bg:var(--abalone-bg);--bg-dark:var(--abalone-bg-dark);--stripe:var(--abalone-stripe);--panel:var(--abalone-panel);--ribbon:var(--abalone-ribbon);--ribbon-dark:var(--abalone-ribbon-dark);--dot:var(--abalone-dot)}
  .label--salted{top:680px;--bg:var(--salted-bg);--bg-dark:var(--salted-bg-dark);--stripe:var(--salted-stripe);--panel:var(--salted-panel);--ribbon:var(--salted-ribbon);--ribbon-dark:var(--salted-ribbon-dark);--dot:var(--salted-dot)}

  .label__backdrop{position:absolute;inset:0;
    background:radial-gradient(circle at 80% 70%,rgba(255,255,255,.18) 0 60px,transparent 62px),
               radial-gradient(circle at 93% 30%,rgba(0,0,0,.08) 0 55px,transparent 57px),
               radial-gradient(circle at 30% 80%,rgba(0,0,0,.07) 0 50px,transparent 52px);}
  .label__stripe{position:absolute;left:0;right:0;height:10px;background:var(--stripe)}
  .label__stripe--top{top:0}
  .label__stripe--bottom{bottom:0}

  .nutrition{
    position:absolute;left:26px;top:30px;width:250px;height:210px;
    background:var(--panel);border-radius:12px;padding:9px 12px;font-size:7.4px;line-height:1.18;
  }
  .nutrition__title{font-weight:700;font-size:11.5px;line-height:1.1}
  .nutrition__serving{font-size:8px;margin-bottom:5px}
  .nutrition__table{display:grid;grid-template-columns:1fr 28px 1.15fr 30px;column-gap:3px;margin-bottom:5px;white-space:nowrap}
  .nutrition__table b{font-weight:700}
  .nutrition__table .sub{padding-left:8px}
  .nutrition__ingredients{margin-bottom:5px}
  .nutrition__line{white-space:nowrap}
  .nutrition__packer{display:flex;justify-content:space-between;white-space:nowrap}
  .nutrition__footer{position:absolute;left:12px;right:12px;bottom:9px}

  .nut-photo{
    position:absolute;left:325px;top:14px;width:232px;height:232px;border-radius:50%;
    background:radial-gradient(circle at 35% 35%,var(--cream) 0%,#e9cd8d 45%,var(--tan) 100%);
  }
  .brand-title{position:absolute;left:325px;top:34px;width:232px;text-align:center}
  .brand-title__kicker{font-family:"Fredoka",sans-serif;font-weight:600;color:var(--title-navy);font-size:13px;letter-spacing:.5px}
  .brand-title__name{font-family:"Chewy","Fredoka",sans-serif;color:var(--title-orange);font-size:40px;line-height:.95;letter-spacing:1px}

  .ribbon{position:absolute;left:300px;top:150px;width:340px;height:104px}
  .ribbon__text{position:absolute;left:318px;top:180px;width:250px;text-align:center;white-space:nowrap;
    font-family:"Fredoka",sans-serif;font-weight:600;color:#fff;font-size:21px;transform:rotate(-7deg)}
  .net-weight{position:absolute;left:590px;top:158px;width:40px;height:40px;border-radius:50%;
    background:var(--dot);color:#fff;font-size:8px;display:flex;align-items:center;justify-content:center;font-weight:700}

  .benefits{position:absolute;left:680px;top:30px}
  .benefits__lead{font-family:"Gochi Hand",cursive;font-size:17px;line-height:1.05;margin-bottom:8px}
  .label--abalone .benefits__lead,.label--abalone .benefits__list{color:#fff}
  .benefits__list{list-style:none;font-family:"Roboto Condensed",sans-serif;font-size:18px}
  .benefits__list li{display:flex;align-items:center;gap:7px;margin-bottom:3px}
  .benefits__list strong{font-weight:700}
  .tick{width:16px;height:16px;flex:none}
  .label--abalone .tick rect{fill:#fff;stroke:var(--ink)}
  .label--abalone .tick path{stroke:var(--ink)}

  .barcode-space{position:absolute;right:26px;bottom:28px;width:150px;height:62px}
</style>
</head>
<body>

<!-- Wasabi -->
<section class="label label--wasabi">
  <div class="label__backdrop" role="img" aria-label="Soft-focus photo of roasted macadamia nuts"></div>
  <div class="label__stripe label__stripe--top"></div>
  <div class="nutrition">
    <div class="nutrition__title">Nutrition Facts</div>
    <div class="nutrition__serving">Serving size: 100g. Servings per container: 2</div>
    <div class="nutrition__table">
      <b>Energy</b><span>3040kj</span><b>Total Carbohydrate</b><span>11.4g</span>
      <b>Protein</b><span>9.2g</span><span class="sub">Dietary Fibre</span><span>1.4g</span>
      <b>Fat (total oils)</b><span>76.4g</span><span class="sub">Sugars</span><span>10g</span>
      <span class="sub">Monounsaturates</span><span>59.6g</span><b>Sodium</b><span>3mg</span>
      <span class="sub">Poly Unsaturates</span><span>3.1g</span><b>Phosphorus</b><span>53mg</span>
      <span class="sub">Saturated</span><span>13.6g</span><b>Calcium</b><span>409mg</span>
      <b>Cholesterol</b><span>Nil</span><b>Potassium</b><span></span>
    </div>
    <p class="nutrition__ingredients"><b>INGREDIENTS:</b> Australian roasted macadamia nuts, wasabi powder, soy powder, flavour enhancers 321, 627 &amp; 361, dairy solids, salt, yeast and/or extracts, herbs &amp; spices, wheat startch, natural and nature flavours, veg powder, food acid 261 and free flow agent 504.</p>
    <div class="nutrition__footer">
      <p class="nutrition__line"><b>PACKED BY:</b> Brindle Ridge Orchard Nut Company</p>
      <p class="nutrition__line">22 Wattle Creek Road, TALLOWOOD, NSW. AUSTRALIA. 2480.</p>
      <div class="nutrition__packer"><span>ABN: 12 345 678 901</span><b>visit: www.brindleridge-example.com</b></div>
    </div>
  </div>
  <div class="nut-photo" role="img" aria-label="Close-up photo of roasted macadamia nuts"></div>
  <div class="brand-title"><div class="brand-title__kicker">AUSTRALIA'S FINEST</div><div class="brand-title__name">MACADAMIA<br>NUTS</div></div>
  <svg class="ribbon" viewBox="0 0 340 104" aria-hidden="true">
    <polygon points="8,80 40,70 44,100 20,104" fill="var(--ribbon-dark)"/>
    <polygon points="30,52 330,18 338,60 36,96" fill="var(--ribbon)"/>
  </svg>
  <div class="ribbon__text">Wassabi Flavoured</div>
  <div class="net-weight">80g Net</div>
  <div class="benefits">
    <p class="benefits__lead">ROASTED MACADAMIA NUTS<br>with wasabi Flavouring</p>
    <ul class="benefits__list">
      <li><svg class="tick" viewBox="0 0 16 16"><rect x="1" y="1" width="14" height="14" fill="none" stroke="currentColor" stroke-width="1.6"/><path d="M3 8l3 4 8-11" fill="none" stroke="currentColor" stroke-width="2.4"/></svg><span><strong>HIGH</strong> in Omega 3</span></li>
      <li><svg class="tick" viewBox="0 0 16 16"><rect x="1" y="1" width="14" height="14" fill="none" stroke="currentColor" stroke-width="1.6"/><path d="M3 8l3 4 8-11" fill="none" stroke="currentColor" stroke-width="2.4"/></svg><span><strong>ZERO</strong> cholesterol</span></li>
      <li><svg class="tick" viewBox="0 0 16 16"><rect x="1" y="1" width="14" height="14" fill="none" stroke="currentColor" stroke-width="1.6"/><path d="M3 8l3 4 8-11" fill="none" stroke="currentColor" stroke-width="2.4"/></svg><span><strong>VITAL SOURCE</strong> of monounsaturates</span></li>
    </ul>
  </div>
  <div class="barcode-space"></div>
</section>

<!-- Abalone -->
<section class="label label--abalone">
  <div class="label__backdrop" role="img" aria-label="Soft-focus photo of roasted macadamia nuts"></div>
  <div class="label__stripe label__stripe--top"></div>
  <div class="label__stripe label__stripe--bottom"></div>
  <div class="nutrition">
    <div class="nutrition__title">Nutrition Facts</div>
    <div class="nutrition__serving">Serving size: 100g. Servings per container: 2</div>
    <div class="nutrition__table">
      <b>Energy</b><span>3040kj</span><b>Total Carbohydrate</b><span>11.4g</span>
      <b>Protein</b><span>9.2g</span><span class="sub">Dietary Fibre</span><span>1.4g</span>
      <b>Fat (total oils)</b><span>76.4g</span><span class="sub">Sugars</span><span>10g</span>
      <span class="sub">Monounsaturates</span><span>59.6g</span><b>Sodium</b><span>241mg</span>
      <span class="sub">Poly Unsaturates</span><span>3.1g</span><b>Phosphorus</b><span>53mg</span>
      <span class="sub">Saturated</span><span>13.6g</span><b>Calcium</b><span>409mg</span>
      <b>Cholesterol</b><span>Nil</span><b>Potassium</b><span></span>
    </div>
    <p class="nutrition__ingredients"><b>INGREDIENTS:</b> Australian roasted macadamia nuts, wasabi powder, soy powder, flavour enhancers 321, 627 &amp; 361, dairy solids, salt, yeast and/or extracts, herbs &amp; spices, wheat startch, natural and nature flavours, veg powder, food acid 261 and free flow agent 504.</p>
    <div class="nutrition__footer">
      <p class="nutrition__line"><b>PACKED BY:</b> Brindle Ridge Orchard Nut Company</p>
      <p class="nutrition__line">22 Wattle Creek Road, TALLOWOOD, NSW. AUSTRALIA. 2480.</p>
      <div class="nutrition__packer"><span>ABN: 12 345 678 901</span><b>visit: www.brindleridge-example.com</b></div>
    </div>
  </div>
  <div class="nut-photo" role="img" aria-label="Close-up photo of roasted macadamia nuts"></div>
  <div class="brand-title"><div class="brand-title__kicker">AUSTRALIA'S FINEST</div><div class="brand-title__name">MACADAMIA<br>NUTS</div></div>
  <svg class="ribbon" viewBox="0 0 340 104" aria-hidden="true">
    <polygon points="8,80 40,70 44,100 20,104" fill="var(--ribbon-dark)"/>
    <polygon points="30,52 330,18 338,60 36,96" fill="var(--ribbon)"/>
  </svg>
  <div class="ribbon__text">Abalone Flavoured</div>
  <div class="net-weight">80g Net</div>
  <div class="benefits">
    <p class="benefits__lead">ROASTED MACADAMIA NUTS</p>
    <ul class="benefits__list">
      <li><svg class="tick" viewBox="0 0 16 16"><rect x="1" y="1" width="14" height="14" fill="none" stroke="currentColor" stroke-width="1.6"/><path d="M3 8l3 4 8-11" fill="none" stroke="currentColor" stroke-width="2.4"/></svg><span><strong>HIGH</strong> in Omega 3</span></li>
      <li><svg class="tick" viewBox="0 0 16 16"><rect x="1" y="1" width="14" height="14" fill="none" stroke="currentColor" stroke-width="1.6"/><path d="M3 8l3 4 8-11" fill="none" stroke="currentColor" stroke-width="2.4"/></svg><span><strong>ZERO</strong> cholesterol</span></li>
      <li><svg class="tick" viewBox="0 0 16 16"><rect x="1" y="1" width="14" height="14" fill="none" stroke="currentColor" stroke-width="1.6"/><path d="M3 8l3 4 8-11" fill="none" stroke="currentColor" stroke-width="2.4"/></svg><span><strong>VITAL SOURCE</strong> of monounsaturates</span></li>
    </ul>
  </div>
  <div class="barcode-space"></div>
</section>

<!-- Roasted and Salted -->
<section class="label label--salted">
  <div class="label__backdrop" role="img" aria-label="Soft-focus photo of roasted macadamia nuts"></div>
  <div class="label__stripe label__stripe--top"></div>
  <div class="label__stripe label__stripe--bottom"></div>
  <div class="nutrition">
    <div class="nutrition__title">Nutrition Facts</div>
    <div class="nutrition__serving">Serving size: 100g. Servings per contain #: 2</div>
    <div class="nutrition__table">
      <b>Energy</b><span>3040kj</span><b>Total Carbohydrate</b><span>11.4g</span>
      <b>Protein</b><span>9.2g</span><span class="sub">Dietary Fibre</span><span>1.4g</span>
      <b>Fat (total oils)</b><span>76.4g</span><span class="sub">Sugars</span><span>10g</span>
      <span class="sub">Monounsaturates</span><span>59.6g</span><b>Sodium</b><span>241mg</span>
      <span class="sub">Poly Unsaturates</span><span>3.1g</span><b>Phosphorus</b><span>53mg</span>
      <span class="sub">Saturated</span><span>13.6g</span><b>Calcium</b><span>409mg</span>
      <b>Cholesterol</b><span>Nil</span><b>Potassium</b><span></span>
    </div>
    <p class="nutrition__ingredients"><b>INGREDIENTS:</b> Australian Roasted Macadamia Nuts, Salt.</p>
    <p class="nutrition__line"><b>PACKED BY:</b> Brindle Ridge Orchard Nut Company</p>
    <div class="nutrition__footer">
      <div class="nutrition__packer"><span>ABN: 12 345 678 901</span><b>visit: www.brindleridge-example.com</b></div>
    </div>
  </div>
  <div class="nut-photo" role="img" aria-label="Close-up photo of roasted macadamia nuts"></div>
  <div class="brand-title"><div class="brand-title__kicker">AUSTRALIA'S FINEST</div><div class="brand-title__name">MACADAMIA<br>NUTS</div></div>
  <svg class="ribbon" viewBox="0 0 340 104" aria-hidden="true">
    <polygon points="8,80 40,70 44,100 20,104" fill="var(--ribbon-dark)"/>
    <polygon points="30,52 330,18 338,60 36,96" fill="var(--ribbon)"/>
  </svg>
  <div class="ribbon__text">Roasted and Salted</div>
  <div class="net-weight">80g Net</div>
  <div class="benefits">
    <p class="benefits__lead">ROASTED MACADAMIA NUTS</p>
    <ul class="benefits__list">
      <li><svg class="tick" viewBox="0 0 16 16"><rect x="1" y="1" width="14" height="14" fill="none" stroke="currentColor" stroke-width="1.6"/><path d="M3 8l3 4 8-11" fill="none" stroke="currentColor" stroke-width="2.4"/></svg><span><strong>HIGH</strong> in Omega 3</span></li>
      <li><svg class="tick" viewBox="0 0 16 16"><rect x="1" y="1" width="14" height="14" fill="none" stroke="currentColor" stroke-width="1.6"/><path d="M3 8l3 4 8-11" fill="none" stroke="currentColor" stroke-width="2.4"/></svg><span><strong>ZERO</strong> cholesterol</span></li>
      <li><svg class="tick" viewBox="0 0 16 16"><rect x="1" y="1" width="14" height="14" fill="none" stroke="currentColor" stroke-width="1.6"/><path d="M3 8l3 4 8-11" fill="none" stroke="currentColor" stroke-width="2.4"/></svg><span><strong>VITAL SOURCE</strong> of monounsaturates</span></li>
    </ul>
  </div>
  <div class="barcode-space"></div>
</section>

</body>
</html>
```